KLOMB Systems website

We need a website design using much of the information on the KLOMB flyer (attached) we just had a PixelBarn designer create. We'd like a WordPress Site, no need for a shopping cart attached to it. It should have an About us page, Book titles page, a blog page, Membership and Navigators pages contact us and privacy policy and terms of services.

```html
<!DOCTYPE html>
<html lang="en">
<head>
<meta charset="utf-8">
<title>KLOMB Systems</title>
<link rel="stylesheet" href="https://fonts.googleapis.com/css2?family=Poppins:wght@500;600;700&family=Roboto:wght@400;500;700&display=swap">
<style>
:root{
  --navy:#2d5592;
  --nav:#3d6198;
  --ink:#333a45;
  --muted:#8a8f96;
  --line:#e4e6ea;
  --soft:#f6f7f9;
  --footer:#2b2b2b;
  --footer-bottom:#1e1e1e;
  --white:#ffffff;
}
*{margin:0;padding:0;box-sizing:border-box}
html,body{width:1200px;height:3125px;overflow:hidden;background:var(--white)}
body{position:relative;font-family:"Roboto",Arial,sans-serif;color:var(--ink)}
.abs{position:absolute}
.head{font-family:"Poppins",Arial,sans-serif}

/* header */
.logo{left:135px;top:14px;font-family:"Poppins",Arial,sans-serif;font-weight:600;font-size:34px;color:var(--navy);letter-spacing:1px;display:flex;align-items:center;gap:10px}
.logo-dot{width:12px;height:12px;border-radius:50%;background:var(--navy)}
.pill{top:25px;height:29px;border-radius:15px;font-size:13px;display:flex;align-items:center;justify-content:center;gap:7px}
.pill-phone{left:806px;width:142px;border:1.5px solid var(--navy);color:var(--ink)}
.pill-member{left:956px;width:111px;background:var(--navy);color:var(--white)}
.navbar{left:0;top:75px;width:1200px;height:40px;background:var(--nav)}
.navbar a{position:absolute;top:13px;font-size:12px;color:var(--white);text-decoration:none;text-transform:uppercase;letter-spacing:.3px}

/* hero */
.hero-photo{left:0;top:115px;width:1200px;height:520px;background:linear-gradient(90deg,#eef1f5 0%,#dfe5ec 30%,#e8edf3 60%,#d9e1ea 85%,#f3f5f8 100%)}
.hero-title{left:0;top:258px;width:1200px;text-align:center;font-weight:700;font-size:38px;line-height:44px;color:var(--navy);letter-spacing:.5px}
.hero-sub{left:330px;top:355px;width:540px;text-align:center;font-size:15px;line-height:25px;color:#5a616b}
.btn{display:flex;align-items:center;justify-content:center;font-size:12px;font-weight:700;letter-spacing:.5px;text-transform:uppercase;border-radius:20px}
.btn-solid{background:var(--navy);color:var(--white)}
.hero-btn{left:562px;top:423px;width:148px;height:34px}
.arrow-round{width:28px;height:28px;border-radius:50%;background:#555b63;display:flex;align-items:center;justify-content:center}

/* welcome */
.welcome-photo{left:133px;top:702px;width:394px;height:256px;background:linear-gradient(135deg,#7c8794,#c8ced6 55%,#9aa4af)}
.play{left:313px;top:813px;width:36px;height:36px;border:2px solid var(--white);border-radius:50%}
.welcome-title{left:577px;top:708px;font-size:19px;font-weight:600;color:var(--ink);letter-spacing:.5px}
.welcome-text{left:577px;top:748px;width:480px;font-size:13px;line-height:19px;color:var(--muted)}
.welcome-text p+p{margin-top:19px}
.welcome-btn{left:581px;top:904px;width:125px;height:34px;gap:8px}
.rule{left:133px;top:1004px;width:934px;height:1px;background:var(--line)}

/* services */
.section-title{left:0;width:1200px;text-align:center;font-size:19px;font-weight:600;color:var(--ink);letter-spacing:.5px}
.card{top:1110px;width:257px;height:319px;border:1px solid var(--line);background:var(--white);text-align:center}
.card-photo{position:absolute;left:0;top:0;width:255px;height:188px}
.card-notch{position:absolute;left:0;top:150px}
.card-icon{position:absolute;left:108px;top:178px;width:40px;height:40px}
.card h3{position:absolute;left:0;top:228px;width:100%;font-family:"Poppins",Arial,sans-serif;font-size:14px;font-weight:600;color:var(--ink)}
.card p{position:absolute;left:14px;top:256px;width:227px;font-size:12px;line-height:19px;color:#555b63}
.side-arrow{top:1252px;color:#b9bdc3;font-size:22px}

/* member band */
.band{left:0;top:1481px;width:1200px;height:354px;background:linear-gradient(120deg,#4b6e9f 0%,#6f8db5 40%,#5c7ca9 70%,#8aa3c3 100%)}
.band-title{left:0;top:1556px;width:1200px;text-align:center;font-size:20px;font-weight:600;color:var(--white);letter-spacing:.5px}
.band-text{left:255px;top:1606px;width:690px;text-align:center;font-size:13px;line-height:25px;color:#eef2f8}
.band-btn{left:512px;top:1710px;width:194px;height:50px;border:2px solid var(--white);border-radius:25px;color:var(--white)}

/* pillars */
.pillars{left:0;top:1835px;width:1200px;height:331px;background:var(--soft)}
.pillars-title{left:0;top:1878px;width:1200px;text-align:center;font-size:19px;font-weight:600;color:var(--ink)}
.pillars-title b{color:var(--navy)}
.pillars-sub{left:390px;top:1921px;width:420px;text-align:center;font-size:12px;line-height:25px;color:#555b63}
.pillar{top:2000px;width:190px;text-align:center}
.pillar svg{display:block;margin:0 auto}
.pillar h4{margin-top:12px;font-size:12px;font-weight:700;color:#555b63;text-transform:uppercase;letter-spacing:.5px}
.pillar p{margin-top:6px;font-size:11.5px;line-height:20px;color:#6a7079}
.pillar-rule{top:2010px;width:1px;height:108px;background:var(--line)}

/* news */
.news{top:2250px;width:296px}
.news-photo{width:296px;height:167px}
.news h3{margin-top:24px;font-family:"Poppins",Arial,sans-serif;font-size:13.5px;font-weight:600;color:var(--ink)}
.news .meta{margin-top:4px;font-size:11px;color:#b0b4ba}
.news p{margin-top:24px;font-size:11.5px;line-height:21px;color:#8a8f96}
.more-btn{left:533px;top:2596px;width:136px;height:33px;border:1px solid #d6d9de;font-size:11px;color:#8a8f96;display:flex;align-items:center;justify-content:center;text-transform:uppercase;letter-spacing:.5px}

/* footer */
.footer{left:0;top:2718px;width:1200px;height:365px;background:var(--footer)}
.foot-h{top:2786px;font-size:11.5px;font-weight:700;color:var(--white);text-transform:uppercase;letter-spacing:.5px}
.foot-t{font-size:12px;line-height:18px;color:#c9ccd0}
.foot-links a{display:block;font-size:12px;line-height:29px;color:#c9ccd0;text-decoration:none}
.news-input{left:604px;top:2868px;width:154px;height:34px;background:var(--white);font-size:11px;color:#b0b4ba;padding:10px 12px}
.news-go{left:758px;top:2868px;width:36px;height:34px;background:var(--navy);display:flex;align-items:center;justify-content:center}
.social{top:2820px;width:28px;height:28px;border-radius:2px}
.foot-bottom{left:0;top:3083px;width:1200px;height:42px;background:var(--footer-bottom)}
.copy{left:135px;top:3098px;font-size:10.5px;color:#9a9ea4}
</style>
</head>
<body>

<!-- header -->
<div class="abs logo"><span class="logo-dot"></span>KLOMB</div>
<div class="abs pill pill-phone">
  <svg width="12" height="12" viewBox="0 0 24 24"><path d="M6.6 10.8a15.1 15.1 0 006.6 6.6l2.2-2.2c.3-.3.7-.4 1-.2 1.1.4 2.3.6 3.6.6.6 0 1 .4 1 1V20c0 .6-.4 1-1 1A17 17 0 013 4c0-.6.4-1 1-1h3.5c.6 0 1 .4 1 1 0 1.3.2 2.5.6 3.6.1.3 0 .7-.2 1z" fill="#333a45"/></svg>
  555-014-2290
</div>
<div class="abs pill pill-member">Membership</div>

<nav class="abs navbar">
  <a style="left:135px">Home</a>
  <a style="left:208px">About Us</a>
  <a style="left:306px">Blog</a>
  <a style="left:381px">Membership</a>
  <a style="left:502px">Privacy Policy</a>
  <a style="left:629px">Contact Us</a>
</nav>

<!-- hero -->
<div class="abs hero-photo" role="img" aria-label="Photo of smiling business team seated in a bright office, with a senior executive standing on the right"></div>
<svg class="abs" style="left:0;top:555px" width="1200" height="82" viewBox="0 0 1200 82">
  <polygon points="0,22 600,78 1200,22 1200,82 0,82" fill="#ffffff"/>
  <polyline points="170,38 600,72 1030,38" fill="none" stroke="#2d5592" stroke-width="3"/>
  <polyline points="420,58 600,78 780,58" fill="none" stroke="#2d5592" stroke-width="5"/>
</svg>
<h1 class="abs head hero-title">ACCURATE YOUR BUSINESS<br>WITH KLOMB</h1>
<p class="abs hero-sub">Lorem ipsum dolor sit amet, consectetuer adipiscing elit. Aenean commodo ligula eget dolor. Aenean massa. Cum sociis natoque penatibus et magnis dis</p>
<div class="abs btn btn-solid hero-btn">Contact Us</div>
<div class="abs arrow-round" style="left:90px;top:338px"><svg width="10" height="12" viewBox="0 0 10 12"><path d="M7 1L2 6l5 5" stroke="#fff" stroke-width="2" fill="none"/></svg></div>
<div class="abs arrow-round" style="left:1084px;top:338px"><svg width="10" height="12" viewBox="0 0 10 12"><path d="M3 1l5 5-5 5" stroke="#fff" stroke-width="2" fill="none"/></svg></div>

<!-- welcome -->
<div class="abs welcome-photo" role="img" aria-label="Photo of colleagues in a meeting around a table"></div>
<div class="abs play"><svg width="32" height="32" viewBox="0 0 32 32"><polygon points="13,10 22,16 13,22" fill="#fff"/></svg></div>
<h2 class="abs head welcome-title">WELCOME TO KLOMB</h2>
<div class="abs welcome-text">
  <p>Donec odio. Quisque volutpat mattis eros. Nullam malesuada erat ut turpis. Suspendisse urna nibh, viverra non, semper suscipit, posuere a, pede. Donec nec justo eget felis facilisis fermentum. Aliquam porttitor mauris sit amet orci. Aenean dignissim pellentesque felis.</p>
  <p>Morbi in sem quis dui placerat ornare. Pellentesque odio nisi, euismod in, pharetra a, ultricies in, diam. Sed arcu. Cras consequat.</p>
</div>
<div class="abs btn btn-solid welcome-btn">Read More <svg width="8" height="10" viewBox="0 0 8 10"><path d="M2 1l4 4-4 4" stroke="#fff" stroke-width="1.8" fill="none"/></svg></div>
<div class="abs rule"></div>

<!-- services -->
<h2 class="abs head section-title" style="top:1048px">KLOMB OFFERING SERVICES</h2>
<div class="abs side-arrow" style="left:104px">&#8249;</div>
<div class="abs side-arrow" style="left:1083px">&#8250;</div>

<div class="abs card" style="left:133px">
  <div class="card-photo" role="img" aria-label="Photo of a business coaching session in an office" style="background:linear-gradient(135deg,#5f6f82,#aebbc9 60%,#7d8a99)"></div>
  <svg class="card-notch" width="255" height="40" viewBox="0 0 255 40"><polygon points="0,18 128,2 255,18 255,40 0,40" fill="#fff"/></svg>
  <svg class="card-icon" viewBox="0 0 40 40"><circle cx="14" cy="20" r="10" fill="none" stroke="#2d5592" stroke-width="2.5"/><circle cx="27" cy="16" r="9" fill="none" stroke="#2d5592" stroke-width="2.5"/></svg>
  <h3>KLOMB COACHING</h3>
  <p>Manage your condo with ease and security. Ensure full receipt of revenue.</p>
</div>
<div class="abs card" style="left:465px">
  <div class="card-photo" role="img" aria-label="Photo of a business handshake over a contract" style="background:linear-gradient(135deg,#c9d4e0,#eef2f6 55%,#b4c2d2)"></div>
  <svg class="card-notch" width="255" height="40" viewBox="0 0 255 40"><polygon points="0,18 128,2 255,18 255,40 0,40" fill="#fff"/></svg>
  <svg class="card-icon" viewBox="0 0 40 40"><rect x="11" y="8" width="18" height="24" rx="2" fill="#2d5592"/><rect x="14" y="12" width="12" height="2" fill="#fff"/></svg>
  <h3>KLOMB STRUCTURE</h3>
  <p>Stop defaulting with our team of qualified professionals.</p>
</div>
<div class="abs card" style="left:810px">
  <div class="card-photo" role="img" aria-label="Photo of a hand with a magnifying glass beside a small tree of images" style="background:linear-gradient(135deg,#e8ecf0,#d0d8e0 50%,#a9b8c6)"></div>
  <svg class="card-notch" width="255" height="40" viewBox="0 0 255 40"><polygon points="0,18 128,2 255,18 255,40 0,40" fill="#fff"/></svg>
  <svg class="card-icon" viewBox="0 0 40 40"><rect x="10" y="10" width="20" height="20" fill="none" stroke="#2d5592" stroke-width="2.2"/><line x1="10" y1="20" x2="30" y2="20" stroke="#2d5592" stroke-width="2"/></svg>
  <h3>KLOMB RESOURCES</h3>
  <p>Complete structure to better serve our customers safely and quickly.</p>
</div>

<!-- member band -->
<div class="abs band" role="img" aria-label="Blue-tinted photo of hands working with charts and a laptop"></div>
<h2 class="abs head band-title">BECOME A KLOMB MEMBER TODAY</h2>
<p class="abs band-text">Donec odio. Quisque volutpat mattis eros. Nullam malesuada erat ut turpis. Suspendisse urna nibh, viverra non, semper suscipit, posuere a, pede. Donec nec justo eget felis facilisis fermentum. Aliquam porttitor mauris sit amet orci. Aenean dignissim pellentesque felis. Morbi in sem quis dui placerat ornare. Pellentesque odio nisi. Cras consequat.</p>
<div class="abs btn band-btn">Get Started</div>

<!-- pillars -->
<div class="abs pillars"></div>
<h2 class="abs head pillars-title"><b>KLOMB</b> = STRATEGY, TEAM, ACTION, ACCOUNTABILITY, RESULTS</h2>
<p class="abs pillars-sub">Business consulting excepteur sint occaecat cupidatat consulting non proident, sunt in culpa qui officia deserunt laborum Market.</p>

<div class="abs pillar" style="left:105px">
  <svg width="40" height="40" viewBox="0 0 40 40"><circle cx="20" cy="20" r="15" fill="none" stroke="#9aa0a8" stroke-width="2.5"/><circle cx="20" cy="20" r="8" fill="none" stroke="#d9412f" stroke-width="3"/><circle cx="20" cy="20" r="3" fill="#d9412f"/></svg>
  <h4>Strategy</h4><p>Long-Term Vision,<br>Tatical Planning</p>
</div>
<div class="abs pillar-rule" style="left:295px"></div>
<div class="abs pillar" style="left:303px">
  <svg width="40" height="40" viewBox="0 0 40 40"><circle cx="11" cy="15" r="5" fill="#2f9a5a"/><circle cx="29" cy="15" r="5" fill="#2f9a5a"/><circle cx="20" cy="13" r="6" fill="#2f9a5a"/><rect x="4" y="22" width="32" height="11" rx="5" fill="#2f9a5a"/></svg>
  <h4>Team</h4><p>Healthy Team Relationship<br>&amp; Deelopment</p>
</div>
<div class="abs pillar-rule" style="left:505px"></div>
<div class="abs pillar" style="left:509px">
  <svg width="40" height="40" viewBox="0 0 40 40"><rect x="13" y="6" width="14" height="22" rx="6" fill="#f0b43a"/><rect x="15" y="26" width="10" height="8" fill="#f0b43a"/></svg>
  <h4>Action</h4><p>Processes to Execute the<br>Vision</p>
</div>
<div class="abs pillar-rule" style="left:703px"></div>
<div class="abs pillar" style="left:707px">
  <svg width="40" height="40" viewBox="0 0 40 40"><circle cx="13" cy="14" r="5" fill="#c9a22d"/><circle cx="27" cy="14" r="5" fill="#c9a22d"/><rect x="5" y="21" width="30" height="12" rx="5" fill="#c9a22d"/></svg>
  <h4>Accountability</h4><p>Tools and Checklists to<br>stay on Track</p>
</div>
<div class="abs pillar-rule" style="left:905px"></div>
<div class="abs pillar" style="left:897px">
  <svg width="40" height="40" viewBox="0 0 40 40"><rect x="8" y="24" width="5" height="10" fill="#2aa7a0"/><rect x="16" y="18" width="5" height="16" fill="#2aa7a0"/><rect x="24" y="12" width="5" height="22" fill="#2aa7a0"/><line x1="6" y1="34" x2="34" y2="34" stroke="#2aa7a0" stroke-width="2"/></svg>
  <h4>Results</h4><p>Dashboard &amp;<br>Metrics</p>
</div>

<!-- news -->
<h2 class="abs head section-title" style="top:2192px">RECENT NEWS</h2>
<article class="abs news" style="left:133px">
  <div class="news-photo" role="img" aria-label="Photo of business people reviewing documents" style="background:linear-gradient(135deg,#6c7b8c,#c2ccd6 55%,#8d99a7)"></div>
  <h3>LOREM IPSUM DOLOR SIT AMET</h3>
  <div class="meta">September 18, 2017 in Photography</div>
  <p>Lorem ipsum dolor sit amet, consectetur adipisicing elit, sed do eiusmod tempor incididunt ut labore et dolore magna aliqua.</p>
</article>
<article class="abs news" style="left:452px">
  <div class="news-photo" role="img" aria-label="Photo of a calculator and paperwork on a desk" style="background:linear-gradient(135deg,#e9dcc4,#f6efe3 55%,#d9c7a8)"></div>
  <h3>LOREM IPSUM DOLOR SIT AMET</h3>
  <div class="meta">September 18, 2017 in Photography</div>
  <p>Lorem ipsum dolor sit amet, consectetur adipisicing elit, sed do eiusmod tempor incididunt ut labore et dolore magna aliqua.</p>
</article>
<article class="abs news" style="left:773px">
  <div class="news-photo" role="img" aria-label="Photo of stacked coins on financial charts" style="background:linear-gradient(135deg,#f3f3f1,#d7cfc4 55%,#b39a7c)"></div>
  <h3>LOREM IPSUM DOLOR SIT AMET</h3>
  <div class="meta">September 18, 2017 in Photography</div>
  <p>Lorem ipsum dolor sit amet, consectetur adipisicing elit, sed do eiusmod tempor incididunt ut labore et dolore magna aliqua.</p>
</article>
<div class="abs more-btn">Show More...</div>

<!-- footer -->
<svg class="abs" style="left:0;top:2680px" width="1200" height="40" viewBox="0 0 1200 40">
  <polygon points="0,38 600,4 1200,38 1200,40 0,40" fill="#2b2b2b"/>
  <polyline points="120,31 600,4 1080,31" fill="none" stroke="#2d5592" stroke-width="4"/>
</svg>
<div class="abs footer"></div>

<h4 class="abs foot-h" style="left:140px">Get in Touch</h4>
<svg class="abs" style="left:140px;top:2830px" width="12" height="16" viewBox="0 0 12 16"><path d="M6 0a6 6 0 00-6 6c0 4.5 6 10 6 10s6-5.5 6-10a6 6 0 00-6-6zm0 8.2A2.2 2.2 0 116 3.8a2.2 2.2 0 010 4.4z" fill="#fff"/></svg>
<p class="abs foot-t" style="left:164px;top:2823px;width:170px">Rua das Palmeiras, 210, Ed. Aurora, 8th floor, rooms 801/802, Centro, Lagoa Nova / MG - CEP: 38400-000</p>
<svg class="abs" style="left:140px;top:2922px" width="13" height="13" viewBox="0 0 24 24"><path d="M6.6 10.8a15.1 15.1 0 006.6 6.6l2.2-2.2c.3-.3.7-.4 1-.2 1.1.4 2.3.6 3.6.6.6 0 1 .4 1 1V20c0 .6-.4 1-1 1A17 17 0 013 4c0-.6.4-1 1-1h3.5c.6 0 1 .4 1 1 0 1.3.2 2.5.6 3.6.1.3 0 .7-.2 1z" fill="#fff"/></svg>
<p class="abs foot-t" style="left:164px;top:2920px;font-size:13px">555-014-2290</p>
<svg class="abs" style="left:140px;top:2962px" width="13" height="10" viewBox="0 0 13 10"><rect width="13" height="10" fill="#fff"/><path d="M0 0l6.5 5L13 0" stroke="#2b2b2b" stroke-width="1.3" fill="none"/></svg>
<p class="abs foot-t" style="left:164px;top:2958px">contact@klomb.com</p>

<h4 class="abs foot-h" style="left:406px">Company Links</h4>
<div class="abs foot-links" style="left:408px;top:2809px">
  <a>About us</a><a>Blog</a><a>Membership</a><a>About us</a><a>Services</a>
</div>

<h4 class="abs foot-h" style="left:598px">Newsletter Signup</h4>
<p class="abs foot-t" style="left:600px;top:2812px;width:210px;font-size:10.5px;text-transform:uppercase">If you want receive our all weekly updates signup below</p>
<div class="abs news-input">Email Address</div>
<div class="abs news-go"><svg width="12" height="12" viewBox="0 0 12 12"><polygon points="0,5 12,0 7,12 6,6" fill="#fff"/></svg></div>

<h4 class="abs foot-h" style="left:852px">Social Links</h4>
<div class="abs social" style="left:854px;background:#3b5998"></div>
<div class="abs social" style="left:893px;background:#1da1f2"></div>
<div class="abs social" style="left:931px;background:#dd4b39"></div>
<div class="abs social" style="left:969px;background:#0077b5"></div>
<div class="abs social" style="left:1008px;background:#d8232a"></div>

<div class="abs foot-bottom"></div>
<p class="abs copy">© Copyright 2018 klomb.com . All rights reserved.</p>

</body>
</html>
```